Counseling Design Website

My husband and I are both counselors and have a business called T & K counseling. We have already purchased a logo from you in October of 2022. We both have expertise in Autism, Dyslexia, ADHD, Couples Counseling, Marriage and Family counseling, and Geriatrics. I would also like to have my forms online. I am planning on using Google sites. I have started a site, but havent gotten very far. I would like to have it created where i can just copy and paste so to speak.
https://pages.brivexa.net/d/47kPzq2Hx8D-LN_cT5uQwE83BVKLpYmda/p/2ZRTe8uPwJ6bxnsr5WLVLOuVVSSQxFBRT/edit

```html
<!DOCTYPE html>
<html lang="en">
<head>
<meta charset="utf-8">
<title>T &amp; K Counselling</title>
<link href="https://fonts.googleapis.com/css2?family=Jost:wght@400;500;600;700&family=Lato:wght@400;700&family=Courgette&display=swap" rel="stylesheet">
<style>
:root{
  --purple:#7b4dfa;
  --purple-dark:#6a3ef0;
  --ink:#111111;
  --text:#2b2b2b;
  --muted:#7a7a7a;
  --field:#f3f3f3;
  --band:#f4f4f4;
  --white:#ffffff;
  --black:#000000;
}
*{margin:0;padding:0;box-sizing:border-box}
html,body{width:1200px;height:3288px;overflow:hidden}
body{position:relative;background:var(--white);font-family:'Lato',sans-serif;color:var(--text)}
.abs{position:absolute}
.script{font-family:'Courgette',cursive;color:var(--purple)}
.heading{font-family:'Jost',sans-serif;font-weight:600;color:var(--ink);letter-spacing:.5px}

/* hero */
.hero{left:0;top:0;width:1200px;height:641px;background:linear-gradient(100deg,#2b3240 0%,#4a4f58 38%,#8a8782 62%,#c9c2b8 85%,#a59f97 100%)}
.hero-shade{left:0;top:0;width:1200px;height:641px;background:linear-gradient(90deg,rgba(20,22,35,.55) 0%,rgba(20,22,35,.25) 50%,rgba(20,22,35,0) 100%)}
.brand{left:138px;top:12px;font-family:'Jost',sans-serif;font-weight:500;font-size:20px;color:var(--white);display:flex;align-items:center;gap:8px}
.brand-dot{width:14px;height:14px;border-radius:50%;background:var(--white)}
.nav a{position:absolute;top:34px;font-size:15px;color:var(--white);text-decoration:none}
.search{left:724px;top:31px;width:210px;height:34px;border-radius:6px;background:rgba(255,255,255,.22);color:#eee;font-size:15px;padding:8px 0 0 24px}
.search svg{position:absolute;right:14px;top:10px}
.login{left:964px;top:24px;width:120px;height:42px;border-radius:6px;background:var(--purple);color:var(--white);font-family:'Jost',sans-serif;font-weight:600;font-size:16px;display:flex;align-items:center;justify-content:center;gap:8px}
.welcome{left:111px;top:250px;font-size:34px}
.hero-title{left:111px;top:298px;font-family:'Jost',sans-serif;font-weight:700;font-size:43px;color:var(--white);letter-spacing:1px}
.hero-text{left:111px;top:356px;font-size:15px;line-height:26px;color:var(--white)}
.btn-light{left:112px;top:425px;width:150px;height:54px;border-radius:5px;background:var(--white);color:var(--purple);font-family:'Jost',sans-serif;font-weight:600;font-size:16px;display:flex;align-items:center;justify-content:center}

/* about */
.about-photo{left:111px;top:716px;width:486px;height:478px;background:linear-gradient(120deg,#5a4a44 0%,#8a7c76 35%,#d8d8da 70%,#f0f0f2 100%)}
.about-kicker{left:631px;top:732px;font-size:19px}
.about-title{left:631px;top:760px;font-size:36px;font-weight:700}
.about-copy{left:631px;top:824px;width:455px;font-size:15px;line-height:25.7px;color:var(--text)}
.about-copy p+p{margin-top:25.7px}
.btn-purple{background:var(--purple);color:var(--white);border-radius:5px;font-family:'Jost',sans-serif;font-weight:600;font-size:16px;display:flex;align-items:center;justify-content:center;letter-spacing:.3px}
.about-btn{left:627px;top:1108px;width:157px;height:56px}

/* services */
.services{left:0;top:1280px;width:1200px;height:833px;background:var(--band)}
.center{left:0;width:1200px;text-align:center}
.svc-kicker{top:1350px;font-size:18px}
.svc-title{top:1380px;font-size:31px;font-weight:500}
.card{width:304px;height:271px;border:5px solid var(--white);display:flex;align-items:flex-end;justify-content:center;padding-bottom:34px;font-family:'Jost',sans-serif;font-weight:600;font-size:19px;color:var(--white);text-align:center;line-height:26px;text-shadow:0 1px 3px rgba(0,0,0,.4)}

/* contact */
.ct-kicker{top:2193px;font-size:18px}
.ct-title{top:2218px;font-size:36px;font-weight:500}
.ct-text{top:2272px;font-size:15px;line-height:23px;color:var(--muted)}
.footer{left:0;top:2784px;width:1200px;height:504px;background:var(--black)}
.form-card{left:179px;top:2358px;width:838px;height:506px;background:var(--white);border-radius:8px;box-shadow:0 4px 24px rgba(0,0,0,.06)}
.field{background:var(--field);border-radius:6px;font-size:12px;color:#666;padding:24px 0 0 26px}
.submit{left:526px;top:2766px;width:133px;height:54px}

/* footer */
.f-brand{left:124px;top:2956px;font-family:'Jost',sans-serif;font-weight:500;font-size:19px;color:var(--purple);display:flex;align-items:center;gap:8px}
.f-brand span.dot{width:12px;height:12px;border-radius:50%;background:var(--purple)}
.social{width:32px;height:32px;border-radius:50%;background:var(--white);top:3102px}
.f-head{top:2948px;font-family:'Jost',sans-serif;font-weight:600;font-size:19px;color:var(--white);letter-spacing:.5px}
.f-link{font-size:15px;color:var(--white)}
.f-row{display:flex;gap:14px;font-size:15px;line-height:24px;color:var(--white)}
.f-row svg{flex:none;margin-top:5px}
.news-input{left:768px;top:3061px;width:274px;height:40px;border-radius:20px;background:var(--white);font-size:15px;color:#999;padding:10px 0 0 20px}
.news-send{right:3px;top:3px;width:34px;height:34px;border-radius:50%;background:var(--purple);position:absolute;display:flex;align-items:center;justify-content:center}
.rule{left:111px;top:3185px;width:978px;height:1px;background:#2a2a2a}
.copy{top:3221px;font-size:15px;color:var(--white)}
</style>
</head>
<body>

<!-- Hero -->
<div class="abs hero" role="img" aria-label="Photo of a counsellor talking with a client in an office"></div>
<div class="abs hero-shade"></div>
<div class="abs brand"><span class="brand-dot"></span>T &amp; K Counseling</div>
<nav class="nav">
  <a href="#" style="left:397px">Home</a>
  <a href="#" style="left:493px">About</a>
  <a href="#" style="left:594px">Project Page</a>
</nav>
<div class="abs search">Search
  <svg width="15" height="15" viewBox="0 0 16 16"><circle cx="6.5" cy="6.5" r="5" fill="none" stroke="#fff" stroke-width="2"/><line x1="10.5" y1="10.5" x2="15" y2="15" stroke="#fff" stroke-width="2.4" stroke-linecap="round"/></svg>
</div>
<div class="abs login">
  <svg width="14" height="16" viewBox="0 0 14 16"><circle cx="7" cy="4.5" r="3.8" fill="#fff"/><path d="M0 16c0-4.5 3-7 7-7s7 2.5 7 7z" fill="#fff"/></svg>LOGIN
</div>
<div class="abs script welcome">Welcome To</div>
<h1 class="abs hero-title">T &amp; K COUNSELLING</h1>
<p class="abs hero-text">Lorem ipsum dolor sit amet, consectetur adipiscing elit,<br>sed do eiusmod tempor incididunt ut labore et dolore</p>
<div class="abs btn-light">GET STARTED</div>

<!-- About -->
<div class="abs about-photo" role="img" aria-label="Photo of a woman on the phone working at a laptop"></div>
<div class="abs script about-kicker">About Us</div>
<h2 class="abs heading about-title">T &amp; K COUNSELLING</h2>
<div class="abs about-copy">
  <p>Lorem ipsum dolor sit amet, consectetur adipiscing elit, sed do eiusmod tempor incididunt ut labore et dolore magna aliqua. Quis ipsum suspendisse ultrices gravida. Risus commodo viverra mae-cenas accumsan lacus vel facilisis.</p>
  <p>Lorem ipsum dolor sit amet, consectetur adipiscing elit, sed do eiusmod tempor incididunt ut labore et dolore magna aliqua. Quis ipsum suspendisse ultrices gravida. Risus commodo viverra mae-cenas accumsan lacus vel facilisis. Lorem ipsum dolor sit amet, consectetur adipiscing elit,</p>
</div>
<div class="abs btn-purple about-btn">LEARN MORE</div>

<!-- Services -->
<div class="abs services"></div>
<div class="abs center script svc-kicker">Our Projects</div>
<h2 class="abs center heading svc-title">OUR SERVICES</h2>
<div class="abs card" style="left:112px;top:1453px;background:linear-gradient(135deg,#6b4a32,#b08a62 50%,#5a6a85)" role="img" aria-label="Photo of a mother and young son">Autism</div>
<div class="abs card" style="left:449px;top:1453px;background:linear-gradient(135deg,#4a4a48,#8c8a86 50%,#c9b8b4)" role="img" aria-label="Photo of two men talking at a table">Dyslexia</div>
<div class="abs card" style="left:785px;top:1453px;background:linear-gradient(135deg,#d8d4cf,#9a8672 50%,#6e6a66)" role="img" aria-label="Photo of a child with a therapist in a classroom">Adhd</div>
<div class="abs card" style="left:112px;top:1754px;background:linear-gradient(135deg,#7a7066,#b4a79a 50%,#4e4c4e)" role="img" aria-label="Photo of a couple embracing on a sofa">Couples Counseling</div>
<div class="abs card" style="left:449px;top:1754px;background:linear-gradient(135deg,#4a3a2e,#9a8e80 50%,#3c3a38)" role="img" aria-label="Photo of a family meeting with a counsellor">Marriage and Family<br>counselling</div>
<div class="abs card" style="left:785px;top:1754px;background:linear-gradient(135deg,#9eb0bf,#5d6e7e 50%,#cfcac4)" role="img" aria-label="Photo of two older women chatting over tea">Geriatrics</div>

<!-- Contact -->
<div class="abs footer"></div>
<div class="abs center script ct-kicker">Contact Us</div>
<h2 class="abs center heading ct-title">GET IN TOUCH</h2>
<p class="abs center ct-text">Lorem ipsum dolor sit amet, consectetur adipiscing elit, sed do eiusmod tempor incididunt ut labore<br>et dolore magna aliqua. Quis ipsum suspendisse ultrices gravida.</p>
<div class="abs form-card"></div>
<div class="abs field" style="left:236px;top:2403px;width:352px;height:61px">Name</div>
<div class="abs field" style="left:608px;top:2403px;width:352px;height:61px">Phone</div>
<div class="abs field" style="left:236px;top:2487px;width:724px;height:61px">Email</div>
<div class="abs field" style="left:236px;top:2571px;width:724px;height:156px">Message</div>
<div class="abs btn-purple submit">SUBMIT</div>

<!-- Footer -->
<div class="abs f-brand"><span class="dot"></span>T &amp; K Counseling</div>
<div class="abs social" style="left:118px"></div>
<div class="abs social" style="left:158px"></div>
<div class="abs social" style="left:197px"></div>
<div class="abs social" style="left:235px"></div>

<div class="abs f-head" style="left:342px">QUICK LINK</div>
<div class="abs f-link" style="left:344px;top:2995px">Home</div>
<div class="abs f-link" style="left:344px;top:3025px">About</div>
<div class="abs f-link" style="left:344px;top:3055px">Project Page</div>

<div class="abs f-head" style="left:516px">CONTACT US</div>
<div class="abs f-row" style="left:518px;top:2993px">
  <svg width="12" height="14" viewBox="0 0 12 16"><path d="M6 0a6 6 0 0 0-6 6c0 4.5 6 10 6 10s6-5.5 6-10a6 6 0 0 0-6-6zm0 8.5A2.5 2.5 0 1 1 6 3.5a2.5 2.5 0 0 1 0 5z" fill="#fff"/></svg>
  <span>48c T &amp; K counselling<br>Lorem ipsum dolor sit</span>
</div>
<div class="abs f-row" style="left:518px;top:3052px">
  <svg width="15" height="12" viewBox="0 0 16 12"><rect width="16" height="12" rx="1.5" fill="#fff"/><path d="M1 1.5l7 5 7-5" fill="none" stroke="#000" stroke-width="1.4"/></svg>
  <span>info@tkcounselling.com</span>
</div>
<div class="abs f-row" style="left:518px;top:3086px">
  <svg width="13" height="13" viewBox="0 0 16 16"><path d="M3.5 0l3 4-2 2.2c1 2.2 2.8 4 5.3 5.3l2.2-2 4 3-1.8 3.2C7.5 15.5.5 8.5.3 1.8z" fill="#fff"/></svg>
  <span>+1 555 014 2273</span>
</div>

<div class="abs f-head" style="left:767px">SUBSCRIBE TO OUR NEWSLETTER</div>
<p class="abs f-link" style="left:770px;top:2993px;line-height:26px">Lorem ipsum dolor sit amet, consectetur<br>adipiscing elit, sed do</p>
<div class="abs news-input">Enter Your Email
  <div class="news-send"><svg width="14" height="14" viewBox="0 0 16 16"><path d="M16 0L0 7l6 2 2 6z" fill="#fff"/></svg></div>
</div>

<div class="abs rule"></div>
<p class="abs center copy">©Copyrights 2023 &nbsp;T &amp; K counselling &nbsp; | &nbsp; All Rights Reserved</p>

</body>
</html>
```